Gobo Flyer to generate sales and to use at trade shows or as a leave behind to client

We are looking to create a flyer to promote our new exterior or interior event lighting options. We are looking for the layout to be clean and consistent with our color scheme. We are a professional technologically advanced company looking to take your event to the next level. We are looking for a layout which has an image at the top as well as a few other images to allow reader to see a few options

Target Market(s)

Residential as well as commercial

Industry/Entity Type

Trade

Requirements
Must have
• Need the round images to create a collage. and include the text samples of what is available

```html
<!DOCTYPE html>
<html lang="en">
<head>
<meta charset="utf-8">
<title>Projected Illuminations Flyer</title>
<link rel="stylesheet" href="https://fonts.googleapis.com/css2?family=Pacifico&family=Lato:ital,wght@0,300;0,400;1,400;1,700&family=Montserrat:ital,wght@0,700;0,800;0,900;1,600&display=swap">
<style>
  :root {
    --page: #e9e9ea;
    --ink: #2b2b2e;
    --ink-soft: #6d6d72;
    --red: #d0142c;
    --blue: #23a3e0;
    --blue-deep: #1479c4;
    --navy: #1d2b3c;
    --white: #ffffff;
    --footer: #0b0b0c;
  }
  * { box-sizing: border-box; margin: 0; padding: 0; }
  html, body { width: 1200px; height: 900px; overflow: hidden; }
  body { background: var(--page); font-family: "Lato", sans-serif; color: var(--ink); }

  .flyer {
    position: absolute; left: 295px; top: 20px;
    width: 610px; height: 860px;
    background: var(--white); overflow: hidden;
    box-shadow: 0 6px 24px rgba(0,0,0,.18);
  }

  .hero-photo {
    position: absolute; left: 0; top: 0; width: 610px; height: 460px;
    background:
      radial-gradient(ellipse 60% 40% at 35% 28%, rgba(200,30,60,.55), transparent 70%),
      radial-gradient(ellipse 55% 25% at 50% 52%, rgba(170,90,200,.65), transparent 75%),
      radial-gradient(circle at 88% 14%, rgba(220,40,40,.5), transparent 25%),
      linear-gradient(180deg, #1a1016 0%, #241426 45%, #2a1a33 70%, #120c16 100%);
  }
  .hero-band { position: absolute; left: 0; top: 0; width: 610px; height: 520px; }

  .title {
    position: absolute; left: 0; top: 0; width: 610px; height: 190px;
    font-family: "Pacifico", cursive; font-weight: 400; color: var(--white);
    text-align: center; line-height: 1;
    text-shadow: 0 2px 6px rgba(0,0,0,.45);
  }
  .title .line-1 { position: absolute; left: 0; right: 0; top: 6px; font-size: 70px; padding-left: 24px; }
  .title .line-2 { position: absolute; left: 0; right: 0; top: 76px; font-size: 74px; }

  .snapshot {
    position: absolute; background: var(--white);
    padding: 8px 8px 14px;
    box-shadow: 0 4px 10px rgba(0,0,0,.35);
  }
  .snapshot .shot {
    width: 100%; height: 100%;
    background:
      radial-gradient(ellipse 70% 35% at 50% 40%, rgba(230,60,200,.8), transparent 70%),
      radial-gradient(ellipse 30% 25% at 85% 45%, rgba(40,80,230,.85), transparent 70%),
      linear-gradient(180deg, #0d0b14 0%, #3b1c4a 45%, #5a4a3c 75%, #2a2520 100%);
  }
  .snapshot .pin {
    position: absolute; top: -6px; left: 50%;
    width: 14px; height: 14px; margin-left: -3px; border-radius: 50%;
    background: radial-gradient(circle at 35% 35%, #9fd8ff, var(--blue-deep));
    box-shadow: 1px 2px 3px rgba(0,0,0,.4);
  }
  .snapshot-1 { left: 22px; top: 282px; width: 186px; height: 178px; transform: rotate(6deg); }
  .snapshot-2 { left: 214px; top: 272px; width: 178px; height: 172px; transform: rotate(1deg); }
  .snapshot-3 { left: 400px; top: 276px; width: 186px; height: 178px; transform: rotate(-6deg); }

  .headline-events {
    position: absolute; left: 0; top: 470px; width: 610px; height: 56px;
    text-align: center; font-weight: 400;
    font-family: "Pacifico", cursive; font-size: 42px; color: var(--red); line-height: 56px;
  }
  .event-types {
    position: absolute; left: 0; top: 530px; width: 610px; text-align: center;
    font-style: italic; font-size: 21px; line-height: 26px; color: #3a3a3e; letter-spacing: -.2px;
  }
  .headline-celebrate {
    position: absolute; left: 0; top: 556px; width: 610px; height: 48px;
    text-align: center; font-weight: 400;
    font-family: "Pacifico", cursive; font-size: 36px; color: var(--blue); line-height: 48px;
  }

  .description {
    position: absolute; left: 50px; top: 622px; width: 290px;
    font-weight: 300; font-size: 14.5px; line-height: 18.8px; color: var(--ink-soft);
  }

  .price-box {
    position: absolute; left: 367px; top: 624px; width: 180px; height: 116px;
    border: 2.5px solid var(--navy); border-radius: 9px; text-align: center;
  }
  .price-box .rent {
    position: absolute; top: -10px; left: 8px; right: 8px;
    background: var(--white); line-height: 16px;
    font-family: "Montserrat", sans-serif; font-weight: 800; font-size: 13px;
    color: var(--blue); letter-spacing: .2px;
  }
  .price-box .as-low {
    margin-top: 9px; font-family: "Montserrat", sans-serif; font-weight: 700; font-size: 12.5px; line-height: 15px;
  }
  .price-box .amount {
    font-family: "Montserrat", sans-serif; font-weight: 900; font-size: 54px;
    color: var(--red); line-height: 52px; letter-spacing: -1px;
  }
  .price-box .terms {
    font-family: "Montserrat", sans-serif; font-style: italic; font-weight: 600;
    font-size: 8.4px; line-height: 11px; color: var(--ink); padding: 1px 6px 0;
  }

  .contact { position: absolute; left: 38px; top: 744px; }
  .contact .phone-row { display: flex; align-items: center; gap: 6px; }
  .contact .phone {
    font-family: "Montserrat", sans-serif; font-weight: 800; font-size: 33px;
    color: var(--blue); letter-spacing: -.5px; line-height: 36px;
  }
  .contact .address { margin: 0 0 0 40px; font-size: 16px; line-height: 20px; color: var(--ink); }

  .brand {
    position: absolute; left: 364px; top: 762px;
    display: flex; align-items: center; gap: 8px;
  }
  .brand .mark { width: 22px; height: 22px; background: var(--navy); }
  .brand .name {
    font-family: "Lato", sans-serif; font-weight: 400; font-size: 15px; line-height: 22px;
    color: var(--navy); letter-spacing: 1px; text-transform: uppercase; white-space: nowrap;
  }

  .footer {
    position: absolute; left: 0; bottom: 0; width: 610px; height: 50px;
    background: var(--footer); color: #a9a9ad;
    display: flex; align-items: center; justify-content: center;
    font-weight: 300; font-size: 19px; letter-spacing: .3px;
  }
</style>
</head>
<body>
  <main class="flyer">
    <div class="hero-photo" role="img" aria-label="Night photo of a house porch lit in purple with red heart light projections and soft bokeh"></div>

    <svg class="hero-band" viewBox="0 0 610 520" aria-hidden="true">
      <defs>
        <linearGradient id="bandBlue" x1="0" y1="0" x2="1" y2="0">
          <stop offset="0" stop-color="#2aa8e6"/>
          <stop offset=".5" stop-color="#1b7fd0"/>
          <stop offset="1" stop-color="#2aa8e6"/>
        </linearGradient>
      </defs>
      <polygon points="0,266 610,250 610,468 0,440" fill="url(#bandBlue)"/>
      <polygon points="0,440 610,468 610,520 0,520" fill="#ffffff"/>
    </svg>

    <h1 class="title">
      <span class="line-1">Projected</span>
      <span class="line-2">Illuminations</span>
    </h1>

    <figure class="snapshot snapshot-1">
      <div class="shot" role="img" aria-label="Photo of a home exterior washed in pink and blue light at night"></div>
      <span class="pin"></span>
    </figure>
    <figure class="snapshot snapshot-2">
      <div class="shot" role="img" aria-label="Photo of a home exterior with red, white and blue lighting at night"></div>
      <span class="pin"></span>
    </figure>
    <figure class="snapshot snapshot-3">
      <div class="shot" role="img" aria-label="Photo of a home lit in magenta with a greeting projected on the driveway"></div>
      <span class="pin"></span>
    </figure>

    <h2 class="headline-events">Perfect for Special Events</h2>
    <p class="event-types">Parties | Graduation | Holidays | Weddings | Business Promotions</p>
    <h2 class="headline-celebrate">Anytime you want to celebrate</h2>

    <p class="description">Illuminate a projected light design and 2 colored wall washers on the exterior or interior of your home business or special event. &nbsp;Choose from many stock designs or customize the image to make the design truly your own.</p>

    <div class="price-box">
      <div class="rent">RENT IT TODAY FOR</div>
      <div class="as-low">as low as</div>
      <div class="amount">$399</div>
      <div class="terms">for a one night rental Including Illuminator, 2 wall washer, Installation and Removal.</div>
    </div>

    <div class="contact">
      <div class="phone-row">
        <svg width="34" height="34" viewBox="0 0 34 34" aria-hidden="true">
          <circle cx="17" cy="17" r="15" fill="none" stroke="#23a3e0" stroke-width="2.5"/>
          <path d="M11.5 9.5c1-.8 2-.6 2.6.3l1.6 2.6c.5.8.3 1.7-.4 2.2l-1.1.8c.8 2 2.4 3.6 4.4 4.5l.8-1.1c.5-.7 1.4-.9 2.2-.4l2.6 1.6c.9.6 1.1 1.6.3 2.6-1.2 1.5-3 2.1-4.8 1.4-4.3-1.7-7.6-5-9.300-9.3-.7-1.8-.1-3.6 1.1-5.2z" fill="#23a3e0"/>
        </svg>
        <span class="phone">555-010-4477</span>
      </div>
      <p class="address">120 Harbor Lane, Brookfield, GA 30000</p>
    </div>

    <div class="brand">
      <span class="mark"></span>
      <span class="name">Lumen Crest Events</span>
    </div>

    <footer class="footer">www.lumencrest-events.com</footer>
  </main>
</body>
</html>
```